LVK delivery van wrap

Need a Torvan 3100 refrigerated van wrapped with. Company logo , company phone number, social media info ,pictures of some of our meals and our 30nightquest logo. Here is out temporary website to give you an idea of our products. http://www.yourleanbistro.example/

Target Market(s)

Everyone that’s is looking for healthy food.

Colors

Designer to choose colors to be used in the design.

Requirements
Must have
• Company Logo, contact info, social media info, website, 30nightquast logo, picture of some of our meals.

```html
<!DOCTYPE html>
<html lang="en">
<head>
<meta charset="utf-8">
<title>LVK delivery van wrap – side panel</title>
<link rel="stylesheet" href="https://fonts.googleapis.com/css2?family=Arimo:ital,wght@0,700;1,700&family=Archivo+Black&display=swap">
<style>
  :root {
    --paper: #ffffff;
    --panel: #fbfbfb;
    --ink: #1c1c1c;
    --orange: #e07f1f;
    --orange-deep: #c9661a;
    --steel: #6d7177;
    --green: #0f4a12;
    --frame: #2a2a2a;
  }
  html, body {
    margin: 0;
    width: 1200px;
    height: 1200px;
    overflow: hidden;
    background: var(--paper);
  }
  .wrap-art { display: block; width: 1200px; height: 1200px; }
  .panel-base { fill: var(--panel); stroke: #d9d9d9; stroke-width: 2; }
  .swoosh-band { fill: var(--orange); }
  .swoosh-line { fill: var(--steel); }
  .social-dot { fill: var(--orange); }
  .emblem-ring { fill: none; stroke: var(--steel); stroke-width: 7; }
  .quest-name { font-family: "Archivo Black", sans-serif; font-size: 34px; fill: var(--ink); }
  .site-url { font-family: "Arimo", sans-serif; font-style: italic; font-weight: 700; font-size: 15px; fill: var(--orange-deep); }
  .phone { font-family: "Arimo", sans-serif; font-style: italic; font-weight: 700; font-size: 44px; fill: #f4f4f4; }
  .brand-name { font-family: "Arimo", sans-serif; font-weight: 700; font-size: 110px; fill: var(--orange); }
  .meal-tile { stroke: var(--frame); stroke-width: 4; }
  .tagline-band { fill: var(--green); stroke: #ffffff; stroke-width: 3; }
  .tagline { font-family: "Arimo", sans-serif; font-weight: 700; font-size: 24px; fill: #ffffff; }
</style>
</head>
<body>
<svg class="wrap-art" viewBox="0 0 1200 1200" xmlns="http://www.w3.org/2000/svg">
  <defs>
    <clipPath id="panel-clip">
      <rect x="50" y="400" width="1100" height="400" rx="24"/>
    </clipPath>
    <linearGradient id="meal-warm" x1="0" y1="0" x2="1" y2="1">
      <stop offset="0" stop-color="#d9b98a"/><stop offset="1" stop-color="#8a5a2e"/>
    </linearGradient>
    <linearGradient id="meal-green" x1="0" y1="0" x2="1" y2="1">
      <stop offset="0" stop-color="#6f9a3a"/><stop offset="1" stop-color="#3d2a22"/>
    </linearGradient>
    <linearGradient id="meal-pale" x1="0" y1="0" x2="1" y2="1">
      <stop offset="0" stop-color="#eeeae2"/><stop offset="1" stop-color="#b8a7a6"/>
    </linearGradient>
    <linearGradient id="meal-red" x1="0" y1="0" x2="1" y2="1">
      <stop offset="0" stop-color="#c23a2a"/><stop offset="1" stop-color="#8a5a24"/>
    </linearGradient>
  </defs>

  <rect class="panel-base" x="50" y="400" width="1100" height="400" rx="24"/>

  <g class="panel-content" clip-path="url(#panel-clip)">
    <!-- brand ring -->
    <circle class="emblem-ring" cx="715" cy="580" r="165"/>

    <!-- lower swoosh -->
    <path class="swoosh-line" d="M270 722 L770 638 L770 646 L285 734 Z"/>
    <path class="swoosh-band" d="M270 800 L270 740 Q540 700 880 680 L905 640 L905 800 Z"/>

    <!-- social -->
    <g class="social-row">
      <circle class="social-dot" cx="120" cy="560" r="11"/>
      <circle class="social-dot" cx="148" cy="560" r="11"/>
      <circle class="social-dot" cx="176" cy="560" r="11"/>
    </g>

    <!-- program name and site -->
    <text class="quest-name" x="218" y="612">30 NIGHT QUEST</text>
    <text class="site-url" x="222" y="642">www.yourleanbistro.example</text>

    <!-- phone -->
    <text class="phone" x="300" y="782">555-014-2287</text>

    <!-- brand name -->
    <text class="brand-name" x="600" y="600" transform="rotate(8 600 560)">LVK</text>

    <!-- meal collage -->
    <g class="meal-collage" transform="rotate(10 1000 600)">
      <rect class="meal-tile" x="880" y="370" width="140" height="110" rx="10" fill="url(#meal-pale)" role="img" aria-label="Photo of grilled chicken in a bowl"/>
      <rect class="meal-tile" x="1030" y="370" width="150" height="130" rx="10" fill="url(#meal-warm)" role="img" aria-label="Photo of a meal prep box with fish and greens"/>
      <rect class="meal-tile" x="890" y="580" width="130" height="100" rx="10" fill="url(#meal-green)" role="img" aria-label="Photo of sliced steak with broccoli"/>
      <rect class="meal-tile" x="1030" y="590" width="160" height="160" rx="10" fill="url(#meal-red)" role="img" aria-label="Photo of a noodle and ground meat meal box"/>
      <rect class="meal-tile" x="840" y="690" width="130" height="140" rx="10" fill="url(#meal-pale)" role="img" aria-label="Photo of a rice and bean salad"/>
    </g>

    <!-- tagline -->
    <g class="tagline-group" transform="rotate(9 790 460)">
      <rect class="tagline-band" x="790" y="460" width="400" height="46" rx="6"/>
      <text class="tagline" x="808" y="491">Your healthy eating alternative</text>
    </g>
  </g>
</svg>
</body>
</html>
```